PostPeddle Social Sharing Platform Needs a Redesign (2 pages / Design only)

PostPeddle is a popular social sharing platform for bloggers and marketers. The site has been quite popular for a few years now, but the site's design is looking quite dated. We're looking for a brand new design to give the service a facelift.

We are looking for a modern and fresh design that keeps all the existing functionality intact. Would prefer designs that incorporate the color blue in them.

We would like the two attached screenshots to be redesigned and submitted - using he same content. Please do not submit a redesign of the front page (non-logged in version). Redesign the 2 attached pages only, and the final deliverable is these two pages as layered PSD files.

Target Market(s)

bloggers, internet marketers

Industry/Entity Type

Social

Number of Pages Required

2 page

Requirements
Must have
• All existing functionality must be intact as seen from the screenshots.
Should not have
• Please do not submit designs based on existing front page (non-logged in version). Use attached screenshots (file 1 and 2) as a guide of existing functionality.

```html
<!DOCTYPE html>
<html lang="en">
<head>
<meta charset="utf-8">
<title>PostPeddle Dashboard</title>
<link rel="stylesheet" href="https://fonts.googleapis.com/css2?family=Open+Sans:wght@400;600;700&display=swap">
<style>
:root{
  --brand:#0d5fa6;
  --ink:#222;
  --muted:#555;
  --line:#d9d9d9;
  --panel:#f5f5f5;
  --slate:#3a434c;
  --footer:#4a4a4a;
  --notice-bg:#f6eeb8;
  --notice-border:#e0d38b;
  --notice-ink:#9a6a16;
  --notice-icon:#f0a030;
  --lime:#9bc21a;
  --pale:#f3f7fb;
  --tag:#3592d6;
}
*{box-sizing:border-box;margin:0;padding:0}
html,body{width:986px;height:1200px;overflow:hidden}
body{font-family:"Open Sans",Arial,sans-serif;color:var(--ink);background:#fff;position:relative;font-size:12px}
.abs{position:absolute}

.topbar{left:0;top:0;width:986px;height:42px;background:var(--brand);border-bottom:3px solid #1d1d1d}
.brand{left:130px;top:0;width:195px;height:40px;background:#fff;display:flex;align-items:center;gap:8px;padding-left:12px}
.brand-dot{width:14px;height:14px;background:var(--brand);border-radius:50%}
.brand-name{font-size:23px;font-weight:700;color:var(--brand);letter-spacing:-.5px}
.logout{left:606px;top:13px;color:#fff;font-weight:700;font-size:12px;display:flex;gap:5px;align-items:center}
.user-avatar{left:713px;top:6px;width:30px;height:30px;border-radius:50%;background:linear-gradient(#c9a48a,#7a5a48);border:2px solid #fff}
.user-avatar-bar{left:709px;top:39px;width:40px;height:3px;background:var(--lime)}
.user-name{left:758px;top:13px;color:#fff;font-weight:600;font-size:12px}

.mainnav{left:129px;top:62px;width:726px;height:26px;border-bottom:1px solid var(--line);display:flex;justify-content:space-between;font-size:13px}
.mainnav a{color:var(--ink);text-decoration:none;padding-bottom:6px;text-transform:uppercase}
.mainnav a.active{border-bottom:2px solid var(--ink)}

.notice{left:129px;top:102px;width:537px;height:39px;background:var(--notice-bg);border:1px solid var(--notice-border);display:flex;align-items:center;gap:12px;padding-left:10px;color:var(--notice-ink);font-size:13px}
.notice-icon{width:24px;height:24px;background:var(--notice-icon);display:flex;align-items:center;justify-content:center}

.followers{left:129px;top:161px;width:537px;height:249px;border:2px solid var(--brand);border-top:0}
.followers-head{height:31px;background:var(--brand)}
.follower-grid{display:grid;grid-template-columns:repeat(8,60px);column-gap:4px;row-gap:16px;padding:15px 0 0 16px}
.member{text-align:center}
.member-photo{width:60px;height:50px;border:1px solid var(--line);padding:2px;background:#fff}
.member-photo span{display:block;width:100%;height:100%}
.member-name{font-size:9px;font-weight:600;margin-top:6px;line-height:12px}
.btn-follow{display:inline-block;background:var(--brand);color:#fff;font-size:8px;font-weight:700;padding:1px 6px;margin-top:1px}
.btn-buy{background:var(--lime)}

.filter{left:129px;top:429px;width:537px;height:127px;background:var(--slate);padding:23px 24px}
.filter-inner{background:#fff;height:83px;padding:10px 20px}
.filter-row{display:flex;align-items:center;gap:8px;font-size:11px}
.filter-label{font-weight:700;width:62px}
.select{border:1px solid var(--line);height:24px;padding:4px 8px;font-size:11px;display:flex;justify-content:space-between}
.search{margin-top:6px;border:1px solid var(--line);height:26px;display:flex;align-items:center;justify-content:space-between;padding-left:8px;font-size:11px}
.search-btn{width:28px;height:26px;background:#b5b9bd;display:flex;align-items:center;justify-content:center}

.tweet-avatar{left:129px;width:46px;height:46px;border:1px solid var(--line);padding:2px;background:#fff}
.tweet-avatar span{display:block;width:100%;height:100%}
.tweet{left:186px;width:479px;height:146px;border:1px solid var(--line)}
.tweet.featured{border-color:var(--brand)}
.tweet-body{background:var(--panel);height:95px;padding:22px 30px;font-size:11px;line-height:13px}
.tweet.featured .tweet-body{background:var(--pale)}
.tweet-body b{font-weight:700}
.tweet-body a{color:var(--brand);text-decoration:none}
.tweet-body p{margin-bottom:5px}
.tweet-actions{display:flex;align-items:center;padding:12px 30px;font-size:11px;gap:14px;color:var(--brand)}
.tweet-actions .act{display:flex;align-items:center;gap:4px}
.share{margin-left:auto;display:flex;gap:18px}
.share-btn{display:flex;align-items:center;gap:3px}
.share-label{background:var(--brand);color:#fff;font-size:9px;font-weight:700;padding:1px 5px}
.share-label.alt{background:#fff;color:#c33;border:1px solid var(--line)}
.share-count{border:1px solid #bbb;font-size:9px;color:var(--muted);padding:0 4px}
.featured-tag{left:163px;top:812px;width:21px;height:83px;background:var(--tag);color:#fff;font-size:9px;writing-mode:vertical-rl;transform:rotate(180deg);display:flex;align-items:center;justify-content:center}

.spinner{left:409px;top:1084px}

.credits{left:682px;top:102px;width:173px;height:142px;background:var(--brand);color:#fff;text-align:center;padding-top:20px}
.credits-num{font-size:29px;line-height:32px}
.credits-label{font-size:14px;opacity:.9}
.credits-cta{font-size:14px}
.credits-cta b{font-weight:700}
.credits-big{font-size:17px;font-weight:700}
.engage{left:682px;top:262px;width:173px;height:229px;background:var(--pale);border:1px solid #e4ebf2;text-align:center;padding-top:10px}
.engage h3{font-size:11px;font-weight:600;line-height:13px;padding:0 8px}
.engage-grid{display:grid;grid-template-columns:repeat(3,44px);gap:12px 11px;justify-content:center;margin-top:12px}
.placeholder{width:44px;height:42px;border:1px solid var(--line);background:#fff;padding:3px}
.placeholder span{display:block;width:100%;height:100%;background:#cfd2d5}
.engage .member-name{font-size:9px;margin-top:4px}
.featured-sites{left:682px;top:511px;width:173px;height:465px;border:1px solid var(--line)}
.featured-head{height:24px;background:#5c5c5c;color:#fff;font-size:12px;text-align:center;line-height:24px}
.site{padding:10px 12px 0}
.site h4{font-size:11px;font-weight:600;line-height:13px}
.site-shot{width:148px;height:110px;margin-top:6px;border:1px solid var(--line)}
.site p{font-size:9px;line-height:12px;margin-top:8px}
.site + .site{border-top:1px solid var(--line);margin:12px 12px 0;padding:10px 0 0}

.back-top{left:907px;top:1088px;width:79px;height:36px;background:var(--brand);color:#fff;font-size:10px;text-align:center;line-height:12px;padding-top:6px}
.footer{left:0;top:1124px;width:986px;height:76px;background:var(--footer);color:#ddd;font-size:9px;text-align:center;padding-top:24px;line-height:15px}
</style>
</head>
<body>

<header class="abs topbar"></header>
<div class="abs brand"><span class="brand-dot"></span><span class="brand-name">PostPeddle</span></div>
<div class="abs logout">Logout
  <svg width="12" height="12" viewBox="0 0 12 12"><rect x="1" y="5" width="10" height="7" fill="#fff"/><path d="M3 5V3a3 3 0 0 1 6 0" stroke="#fff" stroke-width="1.5" fill="none"/></svg>
</div>
<div class="abs user-avatar" role="img" aria-label="Member profile photo"></div>
<div class="abs user-avatar-bar"></div>
<div class="abs user-name">Danmerrow</div>

<nav class="abs mainnav">
  <a class="active">Dashboard</a><a>Flocker Followers</a><a>Submit Tweet</a><a>Activity Summary</a><a>Buy Credots</a><a>Settings</a><a>Affiliates</a>
</nav>

<div class="abs notice">
  <span class="notice-icon"><svg width="14" height="12" viewBox="0 0 14 12"><path d="M1 4h3l6-3v10L4 8H1z" fill="#fff"/></svg></span>
  See who won our contest Click here
</div>

<section class="abs followers">
  <div class="followers-head"></div>
  <div class="follower-grid">
    <div class="member"><div class="member-photo"><span role="img" aria-label="Member avatar, cartoon character" style="background:#2f8fc7"></span></div><div class="member-name">name here</div><span class="btn-follow">follow</span></div>
    <div class="member"><div class="member-photo"><span role="img" aria-label="Member photo" style="background:#6b7a8a"></span></div><div class="member-name">name here</div><span class="btn-follow">follow</span></div>
    <div class="member"><div class="member-photo"><span role="img" aria-label="Member photo" style="background:#8a5236"></span></div><div class="member-name">name here</div><span class="btn-follow">follow</span></div>
    <div class="member"><div class="member-photo"><span role="img" aria-label="Member avatar, colourful flower graphic" style="background:linear-gradient(135deg,#f3c43b,#e96a8e,#5aa9e6)"></span></div><div class="member-name">name here</div><span class="btn-follow">follow</span></div>
    <div class="member"><div class="member-photo"><span role="img" aria-label="Member photo" style="background:#8c6f5e"></span></div><div class="member-name">name here</div><span class="btn-follow">follow</span></div>
    <div class="member"><div class="member-photo"><span role="img" aria-label="Member photo" style="background:#6e3a2c"></span></div><div class="member-name">name here</div><span class="btn-follow">follow</span></div>
    <div class="member"><div class="member-photo"><span role="img" aria-label="Member photo" style="background:#a6674d"></span></div><div class="member-name">name here</div><span class="btn-follow">follow</span></div>
    <div class="member"><div class="member-photo"><span role="img" aria-label="Member group photo" style="background:#4a2a22"></span></div><div class="member-name">name here</div><span class="btn-follow">follow</span></div>

    <div class="member"><div class="member-photo"><span role="img" aria-label="Member avatar, cartoon character" style="background:#2f8fc7"></span></div><div class="member-name">name here</div><span class="btn-follow">follow</span></div>
    <div class="member"><div class="member-photo"><span role="img" aria-label="Member photo" style="background:#6b7a8a"></span></div><div class="member-name">name here</div><span class="btn-follow">follow</span></div>
    <div class="member"><div class="member-photo"><span role="img" aria-label="Member photo" style="background:#8a5236"></span></div><div class="member-name">name here</div><span class="btn-follow">follow</span></div>
    <div class="member"><div class="member-photo"><span role="img" aria-label="Member avatar, colourful flower graphic" style="background:linear-gradient(135deg,#f3c43b,#e96a8e,#5aa9e6)"></span></div><div class="member-name">name here</div><span class="btn-follow">follow</span></div>
    <div class="member"><div class="member-photo"><span role="img" aria-label="Member photo" style="background:#8c6f5e"></span></div><div class="member-name">name here</div><span class="btn-follow">follow</span></div>
    <div class="member"><div class="member-photo"><span role="img" aria-label="Member photo" style="background:#6e3a2c"></span></div><div class="member-name">name here</div><span class="btn-follow">follow</span></div>
    <div class="member"><div class="member-photo"><span role="img" aria-label="Member photo" style="background:#a6674d"></span></div><div class="member-name">name here</div><span class="btn-follow">follow</span></div>
    <div class="member"><div class="member-photo"><span role="img" aria-label="Empty slot placeholder" style="background:#cfd2d5"></span></div><div class="member-name">name here</div><span class="btn-follow btn-buy">buy</span></div>
  </div>
</section>

<section class="abs filter">
  <div class="filter-inner">
    <div class="filter-row">
      <span class="filter-label">Order by:</span>
      <span class="select" style="width:104px">Most Recent <span>▾</span></span>
      <span class="select" style="width:158px">All categories <span>▾</span></span>
    </div>
    <div class="search">
      <span>Search (keyword or Flocker handle)</span>
      <span style="display:flex;align-items:center;gap:8px">
        <svg width="16" height="10" viewBox="0 0 16 10"><path d="M0 1h10M0 5h10M0 9h10" stroke="#aaa" stroke-width="1.2"/><path d="M12 4l2 2 2-2" stroke="#aaa" fill="none"/></svg>
        <span class="search-btn"><svg width="13" height="13" viewBox="0 0 13 13"><circle cx="5.5" cy="5.5" r="4" stroke="#fff" stroke-width="1.6" fill="none"/><path d="M8.5 8.5L12 12" stroke="#fff" stroke-width="1.8"/></svg></span>
      </span>
    </div>
  </div>
</section>

<div class="abs tweet-avatar" style="top:584px"><span role="img" aria-label="Member photo" style="background:#6b7a8a"></span></div>
<article class="abs tweet" style="top:581px">
  <div class="tweet-body">
    <p><b>@BlogGrowthHub</b> is offering 35 credits to promote this <b>(Affiliates)</b></p>
    Here's how to become a trustworthy affiliate <a>http://decksha.re/4kP9mQ</a> via @DeckShare
  </div>
  <div class="tweet-actions">
    <span class="act"><svg width="10" height="10" viewBox="0 0 10 10"><path d="M8 3A3.5 3.5 0 1 0 8.5 6" stroke="#222" stroke-width="1.3" fill="none"/><path d="M6 1l3 1-1 3" fill="#222"/></svg>Report Tweet</span>
    <span class="act"><svg width="10" height="10" viewBox="0 0 10 10"><path d="M1 5h6M5 2l3 3-3 3" stroke="#222" stroke-width="1.5" fill="none"/></svg>Skip this</span>
    <span class="act"><svg width="10" height="10" viewBox="0 0 10 10"><path d="M8 3A3.5 3.5 0 1 0 8.5 6" stroke="#222" stroke-width="1.3" fill="none"/><path d="M6 1l3 1-1 3" fill="#222"/></svg>Shedule Retweet</span>
    <span class="share">
      <span class="share-btn"><span class="share-label">Like</span><span class="share-count">11</span></span>
      <span class="share-btn"><span class="share-label alt">Share</span><span class="share-count">6</span></span>
    </span>
  </div>
</article>

<div class="abs tweet-avatar" style="top:752px"><span role="img" aria-label="Member photo" style="background:#a6674d"></span></div>
<article class="abs tweet featured" style="top:749px">
  <div class="tweet-body">
    <p><b>@BlogGrowthHub</b> is offering 35 credits to promote this <b>(Affiliates)</b></p>
    Here's how to become a trustworthy affiliate <a>http://decksha.re/4kP9mQ</a> via @DeckShare
  </div>
  <div class="tweet-actions">
    <span class="act"><svg width="10" height="10" viewBox="0 0 10 10"><path d="M8 3A3.5 3.5 0 1 0 8.5 6" stroke="#222" stroke-width="1.3" fill="none"/><path d="M6 1l3 1-1 3" fill="#222"/></svg>Report Tweet</span>
    <span class="act"><svg width="10" height="10" viewBox="0 0 10 10"><path d="M1 5h6M5 2l3 3-3 3" stroke="#222" stroke-width="1.5" fill="none"/></svg>Skip this</span>
    <span class="act"><svg width="10" height="10" viewBox="0 0 10 10"><path d="M8 3A3.5 3.5 0 1 0 8.5 6" stroke="#222" stroke-width="1.3" fill="none"/><path d="M6 1l3 1-1 3" fill="#222"/></svg>Shedule Retweet</span>
    <span class="share">
      <span class="share-btn"><span class="share-label">Like</span><span class="share-count">11</span></span>
      <span class="share-btn"><span class="share-label alt">Share</span><span class="share-count">6</span></span>
    </span>
  </div>
</article>
<div class="abs featured-tag">Featured Tweet</div>

<div class="abs tweet-avatar" style="top:920px"><span role="img" aria-label="Member photo" style="background:#8a5236"></span></div>
<article class="abs tweet" style="top:917px">
  <div class="tweet-body">
    <p><b>@BlogGrowthHub</b> is offering 35 credits to promote this <b>(Affiliates)</b></p>
    Here's how to become a trustworthy affiliate <a>http://decksha.re/4kP9mQ</a> via @DeckShare
  </div>
  <div class="tweet-actions">
    <span class="act"><svg width="10" height="10" viewBox="0 0 10 10"><path d="M8 3A3.5 3.5 0 1 0 8.5 6" stroke="#222" stroke-width="1.3" fill="none"/><path d="M6 1l3 1-1 3" fill="#222"/></svg>Report Tweet</span>
    <span class="act"><svg width="10" height="10" viewBox="0 0 10 10"><path d="M1 5h6M5 2l3 3-3 3" stroke="#222" stroke-width="1.5" fill="none"/></svg>Skip this</span>
    <span class="act"><svg width="10" height="10" viewBox="0 0 10 10"><path d="M8 3A3.5 3.5 0 1 0 8.5 6" stroke="#222" stroke-width="1.3" fill="none"/><path d="M6 1l3 1-1 3" fill="#222"/></svg>Shedule Retweet</span>
    <span class="share">
      <span class="share-btn"><span class="share-label">Like</span><span class="share-count">11</span></span>
      <span class="share-btn"><span class="share-label alt">Share</span><span class="share-count">6</span></span>
    </span>
  </div>
</article>

<svg class="abs spinner" width="24" height="24" viewBox="0 0 24 24" aria-label="Loading">
  <g stroke="#555" stroke-width="2.2" stroke-linecap="round">
    <path d="M12 2v4"/><path d="M19 5l-3 3" opacity=".9"/><path d="M22 12h-4" opacity=".8"/><path d="M19 19l-3-3" opacity=".7"/>
    <path d="M12 22v-4" opacity=".55"/><path d="M5 19l3-3" opacity=".4"/><path d="M2 12h4" opacity=".3"/><path d="M5 5l3 3" opacity=".2"/>
  </g>
</svg>

<aside class="abs credits">
  <div class="credits-num">315959</div>
  <div class="credits-label">YOUR CREDITS</div>
  <div class="credits-cta"><b>cick here</b> to submit</div>
  <div class="credits-big">A Retweet</div>
</aside>

<aside class="abs engage">
  <h3>Engage with other members who have recently shared your tweets</h3>
  <div class="engage-grid">
    <div class="member"><div class="placeholder"><span role="img" aria-label="Member placeholder avatar"></span></div><div class="member-name">name</div><span class="btn-follow">follow</span></div>
    <div class="member"><div class="placeholder"><span role="img" aria-label="Member placeholder avatar"></span></div><div class="member-name">name</div><span class="btn-follow">follow</span></div>
    <div class="member"><div class="placeholder"><span role="img" aria-label="Member placeholder avatar"></span></div><div class="member-name">name</div><span class="btn-follow">follow</span></div>
    <div class="member"><div class="placeholder"><span role="img" aria-label="Member placeholder avatar"></span></div><div class="member-name">name</div><span class="btn-follow">follow</span></div>
    <div class="member"><div class="placeholder"><span role="img" aria-label="Member placeholder avatar"></span></div><div class="member-name">name</div><span class="btn-follow">follow</span></div>
    <div class="member"><div class="placeholder"><span role="img" aria-label="Member placeholder avatar"></span></div><div class="member-name">name</div><span class="btn-follow">follow</span></div>
  </div>
</aside>

<aside class="abs featured-sites">
  <div class="featured-head">Featured Websites</div>
  <div class="site">
    <h4>Startup Chatter</h4>
    <div class="site-shot" role="img" aria-label="Website screenshot of a business resource blog" style="background:linear-gradient(#3d4750,#6d7f8e 45%,#2a6fae)"></div>
    <p>Business resource &amp; tips for Start Ups, SME's &amp; Entrepreneurs. Business experts, for the business community.</p>
  </div>
  <div class="site">
    <h4>SEO Training &amp; Internet Marketing Blog</h4>
    <div class="site-shot" role="img" aria-label="Website screenshot of a marketing blog" style="background:linear-gradient(#e9edf2,#c9d2dc 40%,#b23a2e 70%,#e7e7e7)"></div>
    <p>SEO Training Blog, With Free SEO Tools, Unique Strategies &amp; Free Video Tutorials</p>
  </div>
</aside>

<div class="abs back-top">BACK<br>TO TOP</div>

<footer class="abs footer">
  Dashboard &nbsp;| &nbsp;Flocker Followers &nbsp;| &nbsp;Submit Tweet &nbsp;| &nbsp;Activity Summary &nbsp;| &nbsp;Buy Credots &nbsp;| &nbsp;Settings &nbsp;| &nbsp;Affiliates<br>
  © 2014. All Rights Reserved
</footer>

</body>
</html>
```